Business Cards Needed For Veterinary Business

Looking for a business card design for a veterinary blood bank. We would like it to be clean and professional on appearance but still warm and inviting. We would like to utilize our logo and similar coloring. We will use our phone number, email, website, employee name, employee title.

We do not want a bunch of animated animal photos but do not need the style to be as clinical as a laboratory or human medical procedure office.

We are looking for some creative ideas to choose from so that we can generate a standout professional business card for our management team to utilize.

Target Market(s)

professionals

Industry/Entity Type

veterinary

Contact Information for Business Card

employee name, employee title, phone number, website URL, email

Font styles to use
Sans Serif

Colors
0054AA
0677BA
7BADD7
CADEEF
E8F1F8
EB3D1F
EC4F4E
F09395
F8D3D4
FCEDEE

Requirements
Nice to have
• creative design
Should not have
• animated photos

```html
<!DOCTYPE html>
<html lang="en">
<head>
<meta charset="utf-8">
<title>Prairie Animal Blood Bank – Business Cards</title>
<link rel="stylesheet" href="https://fonts.googleapis.com/css2?family=Montserrat:wght@400;600;700&display=swap">
<style>
  :root {
    --backdrop: #232323;
    --card-dark: #1c1c1c;
    --card-light: #ffffff;
    --brand-red: #ec1c24;
    --brand-blue: #0054aa;
    --text-light: #ffffff;
    --shadow: rgba(0, 0, 0, 0.55);
  }
  html, body {
    margin: 0;
    padding: 0;
    overflow: hidden;
  }
  body {
    width: 1200px;
    height: 939px;
    background: var(--backdrop);
    position: relative;
    font-family: "Montserrat", sans-serif;
  }
  .card {
    position: absolute;
    width: 520px;
    height: 300px;
    border-radius: 18px;
    overflow: hidden;
    box-shadow: 0 14px 30px var(--shadow);
  }
  /* Back of card */
  .card-back {
    left: 140px;
    top: 120px;
    background: var(--card-dark);
    display: flex;
    align-items: center;
    justify-content: center;
    gap: 16px;
  }
  .brand-dot {
    width: 46px;
    height: 46px;
    border-radius: 50%;
    background: var(--brand-red);
    flex: none;
  }
  .brand-name {
    color: var(--brand-red);
    font-weight: 700;
    font-size: 30px;
    line-height: 1.1;
    letter-spacing: 0.5px;
    margin: 0;
  }
  /* Front of card */
  .card-front {
    left: 540px;
    top: 500px;
    background: var(--card-light);
  }
  .wave {
    position: absolute;
    inset: 0;
    width: 100%;
    height: 100%;
  }
  .front-brand {
    position: absolute;
    left: 40px;
    top: 110px;
    display: flex;
    align-items: center;
    gap: 10px;
  }
  .front-brand .brand-dot {
    width: 30px;
    height: 30px;
  }
  .front-brand .brand-name {
    font-size: 17px;
  }
  .holder {
    position: absolute;
    right: 34px;
    top: 20px;
    text-align: right;
  }
  .holder-name {
    margin: 0;
    color: var(--brand-blue);
    font-weight: 700;
    font-size: 26px;
    line-height: 32px;
    letter-spacing: 0.5px;
  }
  .holder-title {
    margin: 0;
    color: var(--brand-red);
    font-weight: 400;
    font-size: 15px;
    line-height: 18px;
  }
  .contact {
    position: absolute;
    right: 28px;
    bottom: 44px;
    list-style: none;
    margin: 0;
    padding: 0;
    color: var(--text-light);
    font-size: 13px;
    text-align: right;
  }
  .contact li {
    display: flex;
    align-items: center;
    justify-content: flex-end;
    gap: 8px;
    margin-top: 5px;
  }
  .contact svg {
    width: 12px;
    height: 12px;
    fill: var(--text-light);
  }
</style>
</head>
<body>

<section class="card card-back" aria-label="Card back">
  <span class="brand-dot"></span>
  <p class="brand-name">Prairie Animal<br>Blood Bank</p>
</section>

<section class="card card-front" aria-label="Card front">
  <svg class="wave" viewBox="0 0 520 300" preserveAspectRatio="none" aria-hidden="true">
    <path d="M0,258 C160,262 250,235 320,165 C370,115 430,100 520,100 L520,300 L0,300 Z" fill="var(--brand-red)"/>
    <path d="M70,250 C190,248 260,222 315,158 C365,104 430,90 515,90" fill="none" stroke="var(--brand-blue)" stroke-width="5"/>
    <path d="M40,244 C170,242 245,215 295,162" fill="none" stroke="var(--brand-red)" stroke-width="3"/>
    <path d="M370,128 C410,114 455,110 505,110" fill="none" stroke="#ffffff" stroke-width="3"/>
  </svg>

  <div class="front-brand">
    <span class="brand-dot"></span>
    <p class="brand-name">Prairie Animal<br>Blood Bank</p>
  </div>

  <div class="holder">
    <p class="holder-name">DANIEL HART</p>
    <p class="holder-title">Founder &amp; CEO</p>
  </div>

  <ul class="contact">
    <li>(555) 014-2290
      <svg viewBox="0 0 24 24"><path d="M6.6 10.8a15 15 0 0 0 6.6 6.6l2.2-2.2a1 1 0 0 1 1-.25 11.4 11.4 0 0 0 3.6.57 1 1 0 0 1 1 1V20a1 1 0 0 1-1 1A17 17 0 0 1 3 4a1 1 0 0 1 1-1h3.5a1 1 0 0 1 1 1c0 1.25.2 2.450.57 3.6a1 1 0 0 1-.25 1z"/></svg>
    </li>
    <li>info@prairieanimalblood.com
      <svg viewBox="0 0 24 24"><path d="M2 5h20v14H2z M2 5l10 8 10-8" fill="none" stroke="#fff" stroke-width="2"/></svg>
    </li>
    <li>prairieanimalblood.com
      <svg viewBox="0 0 24 24"><circle cx="12" cy="12" r="9" fill="none" stroke="#fff" stroke-width="2"/><path d="M3 12h18M12 3c3 3 3 15 0 18M12 3c-3 3-3 15 0 18" fill="none" stroke="#fff" stroke-width="1.6"/></svg>
    </li>
  </ul>
</section>

</body>
</html>
```